Business Card Design

I need a Business Card that will catch the attention that will not get thrown in a Drawer. I have 23 companies I use for Auto, Home, Life, and Business Insurance. I make sure that people have the best coverage for the $ spent.

Industry/Entity Type

Business

Contact Information for Business Card

Dorlin Insurance Agency, Inc., Marcus Helgren, 4375 West Tamber Lane Marrowfield, Ohio 45192 555-281-7496, www.dorlinagency.example, Friendbook, Linkwork, Circleplus

```html
<!DOCTYPE html>
<html lang="en">
<head>
<meta charset="utf-8">
<title>Dorlin Insurance Agency – Business Card</title>
<link href="https://fonts.googleapis.com/css2?family=Exo+2:wght@300&family=Ubuntu:wght@700&family=Tinos&display=swap" rel="stylesheet">
<style>
  :root {
    --border-green: #1f3f06;
    --field-green: #2f6700;
    --accent-yellow: #ffff00;
    --agency-yellow: #e6e600;
    --text-white: #f2f2f2;
    --divider: #e8eedf;
    --icon-grey: #c9cfc4;
  }
  html, body {
    margin: 0;
    padding: 0;
    width: 1200px;
    height: 703px;
    overflow: hidden;
    background: var(--border-green);
  }
  .card {
    position: relative;
    width: 1200px;
    height: 703px;
    background: var(--border-green);
  }
  .card-field {
    position: absolute;
    left: 44px;
    top: 42px;
    width: 1112px;
    height: 619px;
    background: var(--field-green);
  }
  .logo-placeholder {
    position: absolute;
    left: 0;
    width: 555px;
    top: 300px;
    text-align: center;
    font-family: "Exo 2", sans-serif;
    font-weight: 300;
    font-size: 31px;
    letter-spacing: 5px;
    color: var(--text-white);
  }
  .divider {
    position: absolute;
    left: 599px;
    top: 100px;
    width: 2px;
    height: 500px;
    background: var(--divider);
  }
  .agent-name {
    position: absolute;
    left: 638px;
    top: 120px;
    width: 480px;
    text-align: center;
    margin: 0;
    font-family: "Ubuntu", sans-serif;
    font-weight: 700;
    font-size: 40px;
    color: var(--accent-yellow);
    text-shadow: 2px 3px 3px rgba(0,0,0,0.55);
  }
  .agency-name {
    position: absolute;
    left: 622px;
    top: 186px;
    width: 520px;
    text-align: center;
    margin: 0;
    font-family: "Tinos", serif;
    font-weight: 400;
    font-size: 128px;
    line-height: 1;
    letter-spacing: 2px;
    color: var(--accent-yellow);
  }
  .agency-type {
    position: absolute;
    left: 622px;
    top: 312px;
    width: 520px;
    text-align: center;
    font-family: "Tinos", serif;
    font-size: 30px;
    letter-spacing: 5px;
    color: var(--agency-yellow);
  }
  .contact-list {
    position: absolute;
    left: 626px;
    top: 378px;
    margin: 0;
    padding: 0;
    list-style: none;
    font-family: "Tinos", serif;
    font-size: 22px;
    letter-spacing: 3px;
    color: var(--text-white);
  }
  .contact-item {
    display: flex;
    align-items: flex-start;
    margin-bottom: 22px;
    line-height: 26px;
  }
  .contact-icon {
    width: 30px;
    height: 30px;
    margin-right: 18px;
    flex: none;
  }
  .social-links {
    position: absolute;
    left: 676px;
    top: 552px;
    display: flex;
    gap: 22px;
    font-family: "Tinos", serif;
    font-size: 20px;
    letter-spacing: 1px;
    color: var(--text-white);
  }
  .social-link {
    display: flex;
    align-items: center;
    gap: 8px;
  }
  .social-mark {
    width: 16px;
    height: 16px;
    background: var(--text-white);
  }
</style>
</head>
<body>
  <div class="card">
    <div class="card-field"></div>

    <div class="logo-placeholder">your logo here</div>

    <div class="divider"></div>

    <h2 class="agent-name">MARCUS HELGREN</h2>
    <h1 class="agency-name">DORLIN</h1>
    <div class="agency-type">INSURANCE AGENCY Inc.</div>

    <ul class="contact-list">
      <li class="contact-item">
        <svg class="contact-icon" viewBox="0 0 30 30" aria-hidden="true">
          <circle cx="15" cy="15" r="13" fill="none" stroke="var(--icon-grey)" stroke-width="2"/>
          <path d="M15 7a5 5 0 0 0-5 5c0 4 5 10 5 10s5-6 5-10a5 5 0 0 0-5-5z" fill="var(--icon-grey)"/>
          <circle cx="15" cy="12" r="1.8" fill="var(--field-green)"/>
        </svg>
        <span>4375 West Tamber Lane<br>Marrowfield, Ohio</span>
      </li>
      <li class="contact-item">
        <svg class="contact-icon" viewBox="0 0 30 30" aria-hidden="true">
          <circle cx="15" cy="15" r="13" fill="none" stroke="var(--icon-grey)" stroke-width="2"/>
          <path d="M10 8l3 0 1 4-2 1.5c1 2 2.5 3.5 4.5 4.5L18 16l4 1 0 3c-7 1-13-5-12-12z" fill="var(--icon-grey)"/>
        </svg>
        <span>45192 555-281-7496</span>
      </li>
      <li class="contact-item">
        <svg class="contact-icon" viewBox="0 0 30 30" aria-hidden="true">
          <circle cx="15" cy="15" r="13" fill="none" stroke="var(--icon-grey)" stroke-width="2"/>
          <path d="M15 8l-7 6h2v7h4v-4h2v4h4v-7h2z" fill="var(--icon-grey)"/>
        </svg>
        <span>www.dorlinagency.example</span>
      </li>
    </ul>

    <div class="social-links">
      <span class="social-link"><span class="social-mark"></span>Friendbook</span>
      <span class="social-link"><span class="social-mark"></span>Circleplus</span>
      <span class="social-link"><span class="social-mark"></span>Linkwork</span>
    </div>
  </div>
</body>
</html>
```